A parent Company needs a website as a leading diversified business in industrial Conglomerates in Af

Tesku Group is a private (Holding) limited liability company incorporated under the Companies Code, 1963 (Act 179) in November, 2013 to following the speedy growth in numbers of its current subsidiaries which has been founded several years ago with an emerging force to become one of the largest and a leading diversified business in industrial Conglomerates in Africa.
The Group which is 100% wholly owned indigenous Ghanaian Company focuses on provision of local, value-added products and services that meet the needs of the African population. The Group is headquartered in Accra, Ghana with interests across a range of sectors in Africa.
We are currently into Food & Beverage, Real Estate Development, Transportation, Health Care, Consumer Products Distribution, Agro Processing, Manufacturing, ICT, Exports & Import, and still counting.
In the next 3 years, we shall announce our ambitions to enter Ghana's largest Oil and Gas industry, playing a strategic role in the petroleum sector with strategic alliances, and help build Ghana's biggest and most important Energy sector in the country.
Inspired by billionaires Ned Harlow, Colin Ashdown, and Efemi Okorusa, Tesku Group (Tesku Foundation) is committed to making a name for itself on the philanthropic circuit and has given away privately and still given to the cause to the needy in the society and some specific social causes in Ghana.
The company is managed by a 5 member board and a 2 member advisory experts who are non-board members.
The company has a vision, mission and it is guided by its core values.
We would like to see a designs that is very professional and looks corporate and can attract investors and partners. It must communicate financial safety and growth and must reflect our logo colors.

```html
<!DOCTYPE html>
<html lang="en">
<head>
<meta charset="utf-8">
<title>Tesku Group</title>
<link href="https://fonts.googleapis.com/css2?family=Open+Sans:wght@300;400;600;700&display=swap" rel="stylesheet">
<style>
:root{
  --teal:#39bd9c;
  --teal-dark:#2ea386;
  --ink:#3c4650;
  --muted:#9aa3ab;
  --line:#e4e7ea;
  --paper:#ffffff;
  --mist:#eef1f3;
  --night:#242a30;
  --night-2:#1b2025;
  --hero-a:#0c1d4a;
  --hero-b:#1d4c9a;
  --hero-c:#3f7ccc;
}
*{box-sizing:border-box;margin:0;padding:0}
html,body{width:1200px;height:3789px;overflow:hidden}
body{font-family:"Open Sans",Arial,sans-serif;color:var(--ink);background:var(--paper);position:relative}
section,header,footer{position:absolute;left:0;width:1200px}
.center{text-align:center}
.eyebrow{font-size:12px;color:var(--ink);font-weight:400}
.section-title{font-size:26px;font-weight:300;letter-spacing:1px;text-transform:uppercase;margin-top:8px}
.rule{width:60px;height:1px;background:var(--teal);margin:10px auto 0}
.lede{font-size:11px;color:var(--muted);line-height:19px;width:560px;margin:16px auto 0}

/* hero */
.hero{top:0;height:580px;overflow:hidden}
.hero-photo{position:absolute;inset:0;background:linear-gradient(160deg,var(--hero-a) 0%,var(--hero-b) 45%,var(--hero-c) 70%,#0b1636 100%)}
.hero-nav{position:absolute;top:22px;right:60px;display:flex;gap:22px;font-size:11px;color:#dfe8f5;text-transform:uppercase;letter-spacing:1px}
.brand{position:absolute;top:130px;left:0;width:1200px;display:flex;justify-content:center;align-items:center;gap:10px;color:#fff;font-size:20px;font-weight:600}
.brand-dot{width:18px;height:18px;border-radius:50%;background:var(--teal)}
.hero-title{position:absolute;top:235px;width:1200px;text-align:center;color:#fff;font-weight:300;font-size:44px;line-height:54px;letter-spacing:1px}
.hero-sub{position:absolute;top:355px;width:1200px;text-align:center;color:#d6e2f3;font-size:11px;line-height:18px}
.hero-btn{position:absolute;top:400px;left:552px;width:96px;height:28px;border:1px solid #cfdcf0;color:#fff;font-size:10px;line-height:26px;text-align:center;text-transform:uppercase;letter-spacing:1px}

/* features */
.features{top:580px;height:330px;background:var(--mist)}
.features-wave{position:absolute;bottom:0;left:0}
.feature-row{position:absolute;top:50px;left:190px;width:820px;display:flex;justify-content:space-between}
.feature{width:180px;text-align:center}
.feature-icon{width:42px;height:42px;margin:0 auto;background:#4a545e;border-radius:3px;display:flex;align-items:center;justify-content:center}
.feature h3{font-size:10px;font-weight:600;text-transform:uppercase;margin-top:22px;letter-spacing:.5px}
.feature p{font-size:10px;color:var(--muted);line-height:16px;margin-top:8px}

/* navigation */
.navigation{top:910px;height:440px;padding-top:10px}
.tabs{position:absolute;top:170px;left:250px;width:220px}
.tab{height:40px;margin-bottom:4px;background:var(--mist);display:flex;align-items:center;padding-left:12px;gap:10px;font-size:10px;color:var(--ink)}
.tab small{display:block;font-size:8px;color:var(--muted)}
.tab-icon{width:14px;height:14px;border:1px solid currentColor;border-radius:2px}
.tab.active{background:var(--teal);color:#fff}
.tab.active small{color:#e6f7f2}
.devices{position:absolute;top:165px;left:520px;width:350px;height:190px;background:linear-gradient(135deg,#f4f6f8,#d9e2ea 60%,#c4d2de);border-radius:4px}

/* call strip */
.cta{top:1350px;height:80px;background:linear-gradient(90deg,#2b3035,#4a4f44 50%,#2b3035)}
.cta p{position:absolute;left:240px;top:22px;color:#fff;font-size:12px;line-height:18px}
.cta p small{display:block;color:#b9bfc4;font-size:10px}
.cta-btn{position:absolute;left:860px;top:28px;width:100px;height:24px;background:var(--teal);color:#fff;font-size:10px;text-transform:uppercase;text-align:center;line-height:24px}

/* news */
.news{top:1450px;height:580px;padding-top:10px}
.cards{position:absolute;top:205px;left:232px;width:736px;display:flex;justify-content:space-between}
.card{width:172px;background:var(--mist)}
.card-photo{height:118px}
.card-photo.a{background:linear-gradient(135deg,#3a3320,#b89a2a 60%,#7a6a3a)}
.card-photo.b{background:linear-gradient(135deg,#d9c6a8,#b6622c 55%,#e4d7c2)}
.card-photo.c{background:linear-gradient(135deg,#4f7fbf,#e8e4d8 55%,#c44a32)}
.card-photo.d{background:linear-gradient(135deg,#b6c9d7,#e2d3c0 55%,#8fa3b3)}
.avatar{width:30px;height:30px;border-radius:50%;background:#c9d0d6;border:2px solid #fff;margin:-15px auto 0;position:relative}
.card h4{font-size:9px;font-weight:600;text-transform:uppercase;text-align:center;margin-top:8px}
.card p{font-size:8px;color:var(--muted);line-height:13px;text-align:center;padding:6px 12px 10px}
.card-meta{height:20px;background:#d5dadf;display:flex;justify-content:space-around;align-items:center;font-size:8px;color:#6e7880}
.pager{position:absolute;top:510px;left:582px;display:flex;gap:6px}
.pager span{width:15px;height:15px;background:#dfe3e7}

/* social feed */
.feed{top:2052px;height:40px}
.feed-dot{position:absolute;left:238px;top:8px;width:18px;height:18px;border-radius:50%;background:var(--teal)}
.feed p{position:absolute;left:400px;top:10px;font-size:10px;color:var(--teal)}

/* team */
.team{top:2140px;height:580px}
.portraits{position:absolute;top:200px;left:232px;width:704px;display:grid;grid-template-columns:repeat(3,190px);justify-content:space-between;row-gap:30px}
.portrait{height:160px;background:linear-gradient(160deg,#e8e4df,#c9a98f 55%,#6d5a4e)}
.portrait.alt{background:linear-gradient(160deg,#dad6d0,#b48b6f 55%,#4e3f36)}

/* location */
.location{top:2770px;height:150px}

/* date badge */
.date-badge{position:absolute;top:3015px;left:540px;width:120px;height:120px;border-radius:50%;background:var(--teal);border:6px solid #d4f0e8;color:#fff;text-align:center;padding-top:22px}
.date-badge strong{display:block;font-size:36px;font-weight:300;line-height:40px}
.date-badge span{font-size:9px;text-transform:uppercase;letter-spacing:1px}

/* contact band */
.contact{top:3200px;height:130px;background:var(--teal);display:flex;justify-content:center;gap:170px;padding-top:30px}
.contact-item{width:170px;text-align:center;color:#fff;font-size:10px}
.contact-icon{width:36px;height:36px;margin:0 auto 14px;background:rgba(255,255,255,.18);display:flex;align-items:center;justify-content:center}

/* footer */
.footer{top:3330px;height:340px;background:var(--night);color:#c5ccd2}
.footer-cols{position:absolute;top:30px;left:230px;width:740px;display:flex;justify-content:space-between}
.footer-col{width:220px}
.footer-col h5{font-size:11px;font-weight:400;text-transform:uppercase;letter-spacing:1px;color:#fff;text-align:center;margin-bottom:16px}
.post{display:flex;gap:8px;margin-bottom:10px}
.post-thumb{width:34px;height:26px;background:linear-gradient(135deg,#c88a3c,#e9c67a)}
.post p{font-size:8px;line-height:12px}
.post p small{display:block;color:#7d868e}
.project-grid{display:grid;grid-template-columns:repeat(4,48px);gap:6px;justify-content:center}
.project-grid span{height:40px;background:linear-gradient(135deg,#6c7780,#c8b59a)}
.project-grid span:nth-child(odd){background:linear-gradient(135deg,#3e4a54,#9aa7b0)}
.about-name{display:flex;align-items:center;gap:8px;color:#fff;font-size:16px;font-weight:600;letter-spacing:3px;margin-bottom:10px}
.about-name i{width:14px;height:14px;border-radius:50%;background:var(--teal)}
.footer-col p.about{font-size:8px;line-height:13px;color:#9ea7af}
.social-row{display:flex;gap:6px;margin-top:14px}
.social-row span{width:14px;height:14px;border-radius:50%;background:#3a424a}

/* bottom bar */
.bottom-bar{top:3670px;height:119px;background:linear-gradient(180deg,#15191d,#2d3338 60%,#15191d)}
.bottom-bar p{position:absolute;top:88px;left:240px;font-size:8px;color:#7d868e}
.bottom-links{position:absolute;top:88px;right:240px;display:flex;gap:12px;font-size:8px;color:#7d868e;text-transform:uppercase}
</style>
</head>
<body>

<header class="hero">
  <div class="hero-photo" role="img" aria-label="Night city skyline with illuminated towers and a curving overpass in deep blue tones"></div>
  <nav class="hero-nav"><span>Home</span><span>About</span><span>Sectors</span><span>News</span><span>Contact</span></nav>
  <div class="brand"><i class="brand-dot"></i>Tesku Group</div>
  <h1 class="hero-title">MATHS IS EASY;<br>DESIGN IS HARD</h1>
  <p class="hero-sub">Local value for a growing continent, built on safety and steady growth.<br>Investing across Africa since 2013.</p>
  <div class="hero-btn">Explore</div>
</header>

<section class="features">
  <div class="feature-row">
    <div class="feature">
      <div class="feature-icon"><svg width="18" height="18" viewBox="0 0 18 18"><path d="M9 1c3 2 4 6 3 10H6C5 7 6 3 9 1z" fill="#fff"/><path d="M6 11l-2 4 3-2M12 11l2 4-3-2" fill="#fff"/></svg></div>
      <h3>Blazing fast deployment</h3>
      <p>Quick setup across every subsidiary so new ventures reach market sooner.</p>
    </div>
    <div class="feature">
      <div class="feature-icon"><svg width="18" height="18" viewBox="0 0 18 18"><rect x="5" y="1" width="8" height="16" rx="1.5" fill="none" stroke="#fff" stroke-width="1.5"/><circle cx="9" cy="14" r="1" fill="#fff"/></svg></div>
      <h3>Crisp retina icons</h3>
      <p>Clear on every screen, giving partners a sharp view of our work.</p>
    </div>
    <div class="feature">
      <div class="feature-icon"><svg width="18" height="18" viewBox="0 0 18 18"><path d="M1 8l16-6-5 15-3-6z" fill="none" stroke="#fff" stroke-width="1.5" stroke-linejoin="round"/></svg></div>
      <h3>Lightweight code</h3>
      <p>Lean pages that load fast for investors on any connection speed.</p>
    </div>
    <div class="feature">
      <div class="feature-icon"><svg width="18" height="18" viewBox="0 0 18 18"><circle cx="9" cy="9" r="3" fill="none" stroke="#fff" stroke-width="1.5"/><circle cx="9" cy="9" r="6.5" fill="none" stroke="#fff" stroke-width="2" stroke-dasharray="2.5 2"/></svg></div>
      <h3>Framework source</h3>
      <p>A solid base that scales with our growing family of businesses.</p>
    </div>
  </div>
  <svg class="features-wave" width="1200" height="60" viewBox="0 0 1200 60" preserveAspectRatio="none"><path d="M0 60V30Q600 -10 1200 30V60z" fill="#fff"/></svg>
</section>

<section class="navigation center">
  <p class="eyebrow">We don't designing sites, we craft pages, layers bringing web pages</p>
  <h2 class="section-title">Easiest Navigation</h2>
  <div class="rule"></div>
  <p class="lede">Simple structure lets visitors find every sector, report and contact in a few clicks.<br>Built for clarity, trust and long term growth.</p>
  <div class="tabs">
    <div class="tab"><i class="tab-icon"></i><div>Portfolio<small>Our core sectors</small></div></div>
    <div class="tab active"><i class="tab-icon"></i><div>About Us<small>Board and advisors</small></div></div>
    <div class="tab"><i class="tab-icon"></i><div>Browser Compatibility<small>Works everywhere</small></div></div>
    <div class="tab"><i class="tab-icon"></i><div>Unparalleled Support<small>Always on call</small></div></div>
  </div>
  <div class="devices" role="img" aria-label="Desktop, laptop, tablet and phone screens showing the site layout"></div>
</section>

<section class="cta">
  <p>Buy this item now and you'll get quality product!<small>Partner with a group built on safety and steady growth.</small></p>
  <div class="cta-btn">Buy it</div>
</section>

<section class="news center">
  <p class="eyebrow">Lorem ipsum dolor si amet, consectetur adipiscing elit</p>
  <h2 class="section-title">Recent News</h2>
  <div class="rule"></div>
  <p class="lede">Updates from our subsidiaries in food, real estate, transport, health care and more.<br>Follow the progress of a growing African group.</p>
  <div class="cards">
    <article class="card"><div class="card-photo a" role="img" aria-label="Sports car on a road"></div><div class="avatar"></div><h4>How to create beautiful</h4><p>New transport routes open across the region this quarter.</p><div class="card-meta"><span>12</span><span>04</span><span>31</span></div></article>
    <article class="card"><div class="card-photo b" role="img" aria-label="Bowl of soup on a table"></div><div class="avatar"></div><h4>How to create beautiful</h4><p>Food and beverage arm adds two local product lines.</p><div class="card-meta"><span>09</span><span>02</span><span>18</span></div></article>
    <article class="card"><div class="card-photo c" role="img" aria-label="Picnic setting with fruit"></div><div class="avatar"></div><h4>Why needs Freebies</h4><p>Agro processing plant reaches full seasonal capacity.</p><div class="card-meta"><span>15</span><span>06</span><span>27</span></div></article>
    <article class="card"><div class="card-photo d" role="img" aria-label="Family portrait outdoors"></div><div class="avatar"></div><h4>How to compose Styles</h4><p>Foundation supports community health care outreach.</p><div class="card-meta"><span>11</span><span>03</span><span>22</span></div></article>
  </div>
  <div class="pager"><span></span><span></span></div>
</section>

<section class="feed">
  <i class="feed-dot"></i>
  <p>Tesku Group news feed</p>
</section>

<section class="team center">
  <p class="eyebrow">Lorem ipsum dolor si amet, consectetur adipiscing elit</p>
  <h2 class="section-title">We'll make this design work for you</h2>
  <div class="rule"></div>
  <p class="lede">A five member board and two advisory experts guide our vision, mission and values.<br>Meet the people steering steady growth.</p>
  <div class="portraits">
    <div class="portrait" role="img" aria-label="Portrait of a board member"></div>
    <div class="portrait alt" role="img" aria-label="Portrait of a board member"></div>
    <div class="portrait" role="img" aria-label="Portrait of a board member"></div>
    <div class="portrait alt" role="img" aria-label="Portrait of an advisory expert"></div>
    <div class="portrait" role="img" aria-label="Portrait of an advisory expert"></div>
    <div class="portrait alt" role="img" aria-label="Portrait of a board member"></div>
  </div>
</section>

<section class="location center">
  <p class="eyebrow">Our Location</p>
  <h2 class="section-title">Find me where the greeny resides</h2>
  <div class="rule"></div>
  <p class="lede">Headquartered in Accra, Ghana, with interests across a range of sectors in Africa.</p>
</section>

<div class="date-badge"><strong>27</strong><span>February</span><br><span>2014</span></div>

<section class="contact">
  <div class="contact-item">
    <div class="contact-icon"><svg width="16" height="16" viewBox="0 0 16 16"><path d="M8 15s5-5 5-9a5 5 0 0 0-10 0c0 4 5 9 5 9z" fill="#fff"/><circle cx="8" cy="6" r="2" fill="#39bd9c"/></svg></div>
    14 Palmgrove Road, Accra
  </div>
  <div class="contact-item">
    <div class="contact-icon"><svg width="16" height="16" viewBox="0 0 16 16"><path d="M3 1h3l1 4-2 1c1 2 3 4 5 5l1-2 4 1v3c0 1-1 2-2 2C7 15 1 9 1 3c0-1 1-2 2-2z" fill="#fff"/></svg></div>
    +233 30 555 0142
  </div>
  <div class="contact-item">
    <div class="contact-icon"><svg width="16" height="16" viewBox="0 0 16 16"><rect x="1" y="3" width="14" height="10" fill="none" stroke="#fff" stroke-width="1.5"/><path d="M1 3l7 6 7-6" fill="none" stroke="#fff" stroke-width="1.5"/></svg></div>
    hello@teskugroup.example
  </div>
</section>

<footer class="footer">
  <div class="footer-cols">
    <div class="footer-col">
      <h5>Recent Post</h5>
      <div class="post"><div class="post-thumb" role="img" aria-label="Post thumbnail"></div><p>Lorem ipsum dolor sit amet consectetur<small>March 02, 2014</small></p></div>
      <div class="post"><div class="post-thumb" role="img" aria-label="Post thumbnail"></div><p>Real estate project breaks ground in Accra<small>February 20, 2014</small></p></div>
      <div class="post"><div class="post-thumb" role="img" aria-label="Post thumbnail"></div><p>Foundation expands support to the needy<small>February 11, 2014</small></p></div>
    </div>
    <div class="footer-col">
      <h5>Recent Projects</h5>
      <div class="project-grid" role="img" aria-label="Grid of recent project thumbnails">
        <span></span><span></span><span></span><span></span><span></span><span></span><span></span><span></span><span></span><span></span><span></span><span></span>
      </div>
    </div>
    <div class="footer-col">
      <h5>About Tesku Group</h5>
      <div class="about-name"><i></i>VANTOR</div>
      <p class="about">A Ghanaian holding company with interests in food, real estate, transport, health care, distribution, agro processing, manufacturing, ICT and trade, built to deliver local value across Africa.</p>
      <div class="social-row"><span></span><span></span><span></span><span></span><span></span><span></span><span></span><span></span></div>
    </div>
  </div>
</footer>

<section class="bottom-bar" role="img" aria-label="Dark city skyline strip">
  <p>© 2014 Tesku Group. All rights reserved.</p>
  <div class="bottom-links"><span>Home</span><span>Blog</span><span>Portfolio</span><span>Contact</span><span>Links</span></div>
</section>

</body>
</html>
```